Harrow Lodging Core Values Poster

I would like the layout I put together designed professionally. The poster will be 36" x 24" in landscape format. I would like the font to match the Harrow Lodging font in the middle of the poster. Convert the black and white poster into something colorful so that the icons pop and it is suitable for framing. The website is https://www.harrowlodging.example/ for reference.

```html
<!DOCTYPE html>
<html lang="en">
<head>
<meta charset="UTF-8">
<title>Harrow Lodging – Our Core Values</title>
<link rel="stylesheet" href="https://fonts.googleapis.com/css2?family=Cinzel:wght@400;900&family=Nunito:wght@400;800&display=swap">
<style>
  :root {
    --bg: #262728;
    --card: #7dd3ea;
    --card-edge: #e9f7fc;
    --ink: #3b3b3d;
    --white: #ffffff;
    --icon-tint: rgba(255, 255, 255, 0.35);
    --shadow: rgba(0, 0, 0, 0.55);
  }
  * { box-sizing: border-box; margin: 0; padding: 0; }
  html, body {
    width: 1200px;
    height: 800px;
    overflow: hidden;
    background: var(--bg);
  }
  .poster {
    position: relative;
    width: 1200px;
    height: 800px;
    background: var(--bg);
  }
  .brand {
    position: absolute;
    top: 34px;
    left: 0;
    width: 100%;
    text-align: center;
    font-family: "Cinzel", serif;
    font-weight: 400;
    font-size: 34px;
    letter-spacing: 0.32em;
    color: var(--white);
    text-transform: uppercase;
  }
  .title {
    position: absolute;
    top: 136px;
    left: 0;
    width: 100%;
    text-align: center;
    font-family: "Cinzel", serif;
    font-weight: 900;
    font-size: 38px;
    letter-spacing: 0.01em;
    color: var(--white);
  }
  .value-card {
    position: absolute;
    width: 168px;
    height: 245px;
    background: var(--card);
    border: 4px solid var(--card-edge);
    border-radius: 36px;
    box-shadow: 6px 8px 18px var(--shadow);
    display: flex;
    flex-direction: column;
    align-items: center;
    padding-top: 18px;
    font-family: "Nunito", sans-serif;
    color: var(--ink);
    text-align: center;
  }
  .value-card--respected { left: 198px; top: 230px; }
  .value-card--accommodating { left: 518px; top: 230px; }
  .value-card--community { left: 837px; top: 230px; }
  .value-card--compassionate { left: 37px; top: 525px; }
  .value-card--balance { left: 357px; top: 525px; }
  .value-card--opportunity { left: 677px; top: 525px; }
  .value-card--family { left: 997px; top: 525px; }

  .value-icon {
    width: 92px;
    height: 90px;
    border-radius: 18px;
    background: var(--icon-tint);
  }
  .value-name {
    margin-top: 26px;
    font-weight: 800;
    font-size: 17px;
    line-height: 1;
    white-space: nowrap;
  }
  .value-traits {
    list-style: none;
    margin-top: 9px;
    font-weight: 400;
    font-size: 15px;
    line-height: 22px;
    white-space: nowrap;
  }
</style>
</head>
<body>
<main class="poster">
  <div class="brand">Harrow Lodging</div>
  <h1 class="title">Our Core Values</h1>

  <section class="value-card value-card--respected">
    <div class="value-icon" role="img" aria-label="Line icon of a handshake"></div>
    <h2 class="value-name">Respected</h2>
    <ul class="value-traits"><li>Trusted</li><li>Integrity</li><li>Reputation</li></ul>
  </section>

  <section class="value-card value-card--accommodating">
    <div class="value-icon" role="img" aria-label="Line icon of a hotel building beneath stars"></div>
    <h2 class="value-name">Accommodating</h2>
    <ul class="value-traits"><li>Guest Driven</li><li>Problem Solving</li><li>Above &amp; Beyond</li></ul>
  </section>

  <section class="value-card value-card--community">
    <div class="value-icon" role="img" aria-label="Line icon of a group of people under a heart"></div>
    <h2 class="value-name">Community</h2>
    <ul class="value-traits"><li>Guest Driven</li><li>Problem Solving</li><li>Above &amp; Beyond</li></ul>
  </section>

  <section class="value-card value-card--compassionate">
    <div class="value-icon" role="img" aria-label="Line icon of three people under a speech bubble with a heart"></div>
    <h2 class="value-name">Compassionate</h2>
    <ul class="value-traits"><li>Empathy</li><li>Forgiving</li><li>Listening</li></ul>
  </section>

  <section class="value-card value-card--balance">
    <div class="value-icon" role="img" aria-label="Line icon of a scale balancing a briefcase and a heart"></div>
    <h2 class="value-name">Balance</h2>
    <ul class="value-traits"><li>Health</li><li>Work-Life</li><li>Happiness</li></ul>
  </section>

  <section class="value-card value-card--opportunity">
    <div class="value-icon" role="img" aria-label="Line icon of rising arrows with a person"></div>
    <h2 class="value-name">Opportunity</h2>
    <ul class="value-traits"><li>Growth</li><li>Successful</li><li>“Plus”-ing</li></ul>
  </section>

  <section class="value-card value-card--family">
    <div class="value-icon" role="img" aria-label="Line icon of a family inside a house with a heart"></div>
    <h2 class="value-name">Family</h2>
    <ul class="value-traits"><li>Caring</li><li>Loyalty</li><li>Tradition</li></ul>
  </section>
</main>
</body>
</html>
```